Branvique needs a business Card Design

We are looking for a business card Design for our new Managed Service Provider Company, Branvique. Branvique encompasses everything IT for the average medium sized business. Our primary services are help desk support, cyber-security (malware and ransomware protection), and Disaster Recovery systems. We would like the design to have a very clean and professional look, with a very minimalist feel.

Target Market(s)

Medium to large sized businesses

Industry/Entity Type

It Service

Contact Information for Business Card

Name GoesHere
name@branvique.com
O: 555-382-6047
C: 555-731-5820

Font styles to use
Other font styles liked:
• Poppins Font Only Please

Colors

Designer to choose only greyscale colors for use in the design.

Requirements
Must have
• Logo included
Nice to have
• Cutting Edge, innovative, minimalistic, elegant

```html
<!DOCTYPE html>
<html lang="en">
<head>
<meta charset="UTF-8">
<title>Branvique Business Card</title>
<link rel="stylesheet" href="https://fonts.googleapis.com/css2?family=Poppins:wght@400;500;600&display=swap">
<style>
  :root {
    --stage: #2b2b2b;
    --navy: #07223a;
    --navy-ink: #142a44;
    --silver: #9aa3ad;
    --paper: #ffffff;
    --grey-text: #2e3640;
    --shadow: rgba(0,0,0,0.45);
  }
  * { margin: 0; padding: 0; box-sizing: border-box; }
  html, body {
    width: 1200px; height: 960px; overflow: hidden;
    background: var(--stage);
    font-family: "Poppins", sans-serif;
  }
  .stage { position: relative; width: 1200px; height: 960px; }
  .card {
    position: absolute;
    width: 630px; height: 360px;
    border-radius: 22px;
    box-shadow: 0 18px 40px var(--shadow);
    overflow: hidden;
  }
  .card-front { left: 80px; top: 70px; background: var(--navy); }
  .card-back { left: 490px; top: 520px; background: var(--paper); }

  .wordmark {
    font-weight: 500;
    letter-spacing: 0.42em;
    text-transform: uppercase;
    white-space: nowrap;
  }
  .card-front .wordmark {
    position: absolute; left: 0; right: 0; top: 158px;
    text-align: center;
    font-size: 34px;
    color: var(--silver);
    padding-left: 0.42em;
  }
  .card-back .wordmark {
    position: absolute; left: 44px; top: 44px;
    font-size: 20px;
    color: var(--navy-ink);
  }
  .person { position: absolute; left: 44px; top: 150px; color: var(--navy-ink); }
  .person-name { font-size: 30px; font-weight: 600; line-height: 1.1; }
  .person-role { font-size: 17px; font-weight: 400; color: var(--grey-text); margin-top: 2px; }
  .contact-list {
    position: absolute; left: 44px; top: 236px;
    list-style: none;
    font-size: 16px; color: var(--grey-text);
  }
  .contact-list li { display: flex; align-items: center; gap: 12px; height: 24px; }
  .contact-list svg { width: 15px; height: 15px; fill: none; stroke: var(--navy-ink); stroke-width: 1.8; }
</style>
</head>
<body>
<main class="stage">
  <section class="card card-front" aria-label="Card front">
    <div class="wordmark">Branvique</div>
  </section>

  <section class="card card-back" aria-label="Card back">
    <div class="wordmark">Branvique</div>
    <div class="person">
      <div class="person-name">Daniel Reyes</div>
      <div class="person-role">Founder</div>
    </div>
    <ul class="contact-list">
      <li>
        <svg viewBox="0 0 16 16"><rect x="4" y="1.5" width="8" height="13" rx="1.5"/><line x1="7" y1="12" x2="9" y2="12"/></svg>
        555-731-5820
      </li>
      <li>
        <svg viewBox="0 0 16 16"><path d="M3 2.5l3 0.5 1 3-1.5 1.2a8 8 0 0 0 3.3 3.3L10 9l3 1 0.5 3-2 1.5C7 14 2 9 1.5 4.5z"/></svg>
        555-382-6047
      </li>
      <li>
        <svg viewBox="0 0 16 16"><rect x="1.5" y="3.5" width="13" height="9" rx="1"/><path d="M1.5 4l6.5 5 6.5-5"/></svg>
        name@branvique.com
      </li>
      <li>
        <svg viewBox="0 0 16 16"><circle cx="8" cy="8" r="6.5"/><path d="M1.5 8h13M8 1.5c2.2 2 2.2 11 0 13M8 1.5c-2.2 2-2.2 11 0 13"/></svg>
        www.branvique.com
      </li>
    </ul>
  </section>
</main>
</body>
</html>
```